Property Management Company looking for a high-end business card, letterhead and envelope design.

We provide high-end / boutique property management for real estate investors or individuals looking for someone to manage their portfolio. we are looking for a cohesive high-end design for our business cards, letterhead and envelopes.

Target Market(s)

Real Estate Investors

Industry/Entity Type

Real Estate

Requirements
Must have
• business card, letterhead and envelope design - logo attached

```html
<!DOCTYPE html>
<html lang="en">
<head>
<meta charset="utf-8">
<title>Clearhold Property Management – Stationery</title>
<link href="https://fonts.googleapis.com/css2?family=Montserrat:wght@600&family=Open+Sans:wght@400&family=Lato:wght@400;700&display=swap" rel="stylesheet">
<style>
  :root {
    --navy: #134a85;
    --navy-faint: #2c5e97;
    --ink: #444;
    --paper: #ffffff;
    --backdrop: #e4e4e4;
    --rule: #1d3f73;
    --mark-faint: #ececec;
  }
  * { margin: 0; padding: 0; box-sizing: border-box; }
  html, body { width: 1200px; height: 1200px; overflow: hidden; background: var(--backdrop); }
  .stage { position: relative; width: 1200px; height: 1200px; }

  .sheet { position: absolute; background: var(--paper); box-shadow: 0 2px 8px rgba(0,0,0,.25); overflow: hidden; }
  .faint-square { position: absolute; background: var(--mark-faint); }

  .brand { font-family: "Montserrat", sans-serif; font-weight: 600; color: var(--navy); text-align: center; line-height: 1; }
  .brand-name { letter-spacing: .18em; }
  .brand-tag { letter-spacing: .2em; margin-top: 3px; }

  /* Letterhead */
  .letterhead { left: 119px; top: 278px; width: 556px; height: 715px; }
  .letterhead .faint-square { left: 154px; top: 232px; width: 250px; height: 250px; }
  .letterhead .brand { position: absolute; top: 18px; left: 0; right: 0; }
  .letterhead .brand-name { font-size: 19px; }
  .letterhead .brand-tag { font-size: 9.5px; }
  .letter { position: absolute; left: 52px; top: 130px; width: 452px; font-family: "Open Sans", sans-serif; font-size: 8.8px; color: var(--ink); }
  .letter p { margin-bottom: 16px; line-height: 16px; }
  .letter .date { margin-bottom: 10px; line-height: 11px; }
  .letter .meta { line-height: 11px; margin-bottom: 28px; }
  .letter .body p { text-align: justify; }
  .letter .closing { margin-top: 32px; margin-bottom: 30px; }
  .signer { font-size: 11.5px; color: #333; line-height: 14px; }
  .signer-role { font-size: 8.8px; margin-top: 4px; }

  .letter-footer { position: absolute; left: 64px; width: 430px; top: 665px; font-family: "Lato", sans-serif; color: #222; text-align: center; }
  .letter-footer .address { font-size: 10.2px; padding-bottom: 2px; border-bottom: 1.5px solid var(--rule); }
  .letter-footer .contact { font-size: 10.2px; margin-top: 5px; white-space: nowrap; margin-left: -4px; margin-right: -4px; }
  .letter-footer b { color: var(--navy); font-weight: 700; }
  .letter-footer .web { color: var(--navy); }

  /* Envelope front */
  .envelope-front { left: 715px; top: 492px; width: 432px; height: 216px; }
  .envelope-front .faint-square { left: 162px; top: 58px; width: 100px; height: 100px; }
  .envelope-front .brand { position: absolute; left: 22px; top: 17px; text-align: left; }
  .envelope-front .brand-name { font-size: 15.5px; }
  .envelope-front .brand-tag { font-size: 7.6px; }
  .envelope-front .return { position: absolute; left: 22px; top: 181px; width: 370px; border-top: 1.5px solid var(--rule); padding-top: 7px; font-family: "Lato", sans-serif; font-size: 8px; color: #222; }

  /* Envelope back */
  .envelope-back { left: 717px; top: 743px; width: 429px; height: 213px; }
  .envelope-back .flap { position: absolute; left: 0; top: 0; width: 429px; height: 51px; }
  .envelope-back .faint-square { left: 161px; top: 79px; width: 100px; height: 100px; }
  .envelope-back .brand { position: absolute; left: 0; right: 0; top: 15px; color: var(--navy-faint); }
  .envelope-back .brand-name { font-size: 15px; }
  .envelope-back .brand-tag { font-size: 7px; }
</style>
</head>
<body>
<main class="stage">

  <section class="sheet letterhead">
    <div class="faint-square" aria-hidden="true"></div>
    <div class="brand">
      <div class="brand-name">CLEARHOLD</div>
      <div class="brand-tag">PROPERTY MANAGEMENT</div>
    </div>

    <div class="letter">
      <p class="date">Issuing Date: May 5, 2018</p>
      <p class="meta">Name Of Employee Mr. XYZABC<br>Address of Employee<br>Address Line 2 etc..</p>
      <p>Dear Mr.XYZABC</p>
      <div class="body">
        <p>Lorem Ipsum has been the industry's standard dummy text ever since the 1500s, when an unknown printer took a galley of type and scrambled it to make a type specimen book. It has survived not only five centuries, but also the leap into electronic typesetting, remaining essentially unchanged. It was popularised in the 1960s with the release of Letraset sheets containing Lorem Ipsum passages, and more recently with desktop publishing software like Aldus PageMaker including versions of Lorem Ipsum.</p>
        <p>Lorem Ipsum is simply dummy text of the printing and typesetting industry. Lorem Ipsum has been the industry's standard dummy text ever since the 1500s, when an unknown printer took a galley of type and scrambled it to make a type specimen book.</p>
        <p>It has survived not only five centuries, but also the leap into electronic typesetting, remaining essentially unchanged. It was popularised in the 1960s with the release of Letraset sheets containing Lorem IpsumIpsum passages.</p>
      </div>
      <p class="closing">Yours Sincerely</p>
      <div class="signer">Daniel Marsh</div>
      <div class="signer-role">Managing Director</div>
    </div>

    <footer class="letter-footer">
      <div class="address">18 Harbor Row, Suite 4, 45452 Eastfield</div>
      <div class="contact"><b>P:</b> 044-555 210 384 | <b>M:</b> 044-555 210 385 | <b>E:</b> hello@clearholdpm.com | www.<span class="web">clearholdpm</span>.com</div>
    </footer>
  </section>

  <section class="sheet envelope-front">
    <div class="faint-square" aria-hidden="true"></div>
    <div class="brand">
      <div class="brand-name">CLEARHOLD</div>
      <div class="brand-tag">PROPERTY MANAGEMENT</div>
    </div>
    <div class="return">18 Harbor Row, Suite 4, Eastfield, 45452</div>
  </section>

  <section class="sheet envelope-back">
    <svg class="flap" viewBox="0 0 429 51" aria-hidden="true">
      <polygon points="0,0 429,0 413,51 16,51" fill="var(--navy)"/>
    </svg>
    <div class="brand">
      <div class="brand-name">CLEARHOLD</div>
      <div class="brand-tag">PROPERTY MANAGEMENT</div>
    </div>
    <div class="faint-square" aria-hidden="true"></div>
  </section>

</main>
</body>
</html>
```